ReDesign Website for a more Bold approach

Hello! I'd like to redesign my website: torvellacapital.com

I'd like to add one thing that's not on my website which is a blog. The design around the blog should be put time into as I will be putting out incredibly great content and want it to attract viewers.

I get a lot of inspiration from quondel.com (the way they flow the big statements across each screen, colors)
amberlit.vc (the simplicity behind the design is beautiful)

I like modern very simple but bold approaches.

I am going to attach my logo here and if it can be thought of when making the design of the website. Thanks!

Industry/Entity Type

Finance and Private Equity

Number of Pages Required

3 page

Font styles to use
Serif
Sans Serif

Colors
0054AA
0677BA
7BADD7
CADEEF
E8F1F8
0094D4
00A9DD
6FCCEA
C7EBF8
E9F6FB
00AB8E
00BBA5
67D7C9
C6EFE9
E9F9F6

Requirements
Must have
• My project must have a Home, Expertise, Story, Clients, Approach, Blog, Contact
Nice to have
• It would be nice to have these tabs reduced to 1-3 pages
Should not have
• My project must not have bright colors.

```html
<!DOCTYPE html>
<html lang="en">
<head>
<meta charset="utf-8">
<title>Torvella Capital</title>
<link href="https://fonts.googleapis.com/css2?family=Lato:wght@400;700;900&family=Montserrat:wght@700&display=swap" rel="stylesheet">
<style>
:root{
  --navy:#0f4aa3;
  --deep:#0d3f98;
  --red:#d8334a;
  --ink:#333;
  --teal:#00ab8e;
  --sky:#c4dcf5;
  --mint:#dff8f4;
  --card-blue:#6b9bd1;
  --card-teal:#5ad2bf;
  --card-cyan:#5bbde6;
  --cyan:#1ea3e0;
  --rule:#ccc;
}
*{margin:0;padding:0;box-sizing:border-box}
html,body{width:1200px;height:4167px;overflow:hidden;background:#fff}
body{position:relative;font-family:'Lato',sans-serif;color:var(--ink)}
.abs{position:absolute}
.logo{left:144px;top:27px;font-family:'Montserrat',sans-serif;font-weight:700;font-size:26px;color:var(--deep);letter-spacing:.3px}
.nav{right:146px;top:30px;display:flex;gap:28px;font-size:15px;color:#222}
.nav a{color:inherit;text-decoration:none;padding-bottom:8px}
.nav a.active{border-bottom:3px solid var(--teal)}
.social{left:1130px;width:14px;height:14px;border-radius:50%;background:#222}
.photo{left:0;width:1056px}
.hero{top:81px;height:530px;background:linear-gradient(135deg,#2a3e78 0%,#6a8bc8 40%,#c9a9d6 65%,#24396e 100%)}
.meeting{top:1662px;height:531px;background:linear-gradient(135deg,#3a4250 0%,#cbb89a 45%,#e8e2d8 60%,#556070 100%)}
.card{background:#fff;box-shadow:0 2px 6px rgba(0,0,0,.15);border-bottom:3px solid #999}
.card h2{position:absolute;font-weight:700;color:var(--navy);font-size:36px;line-height:1}
.card .line{position:absolute;width:65px;height:3px;background:var(--teal)}
.card p{position:absolute;font-size:13.5px;line-height:24px;text-align:justify;color:#444}
.btn{display:flex;height:52px;font-weight:900;font-size:13.5px;color:#fff;text-transform:uppercase}
.btn .plus{width:45px;background:var(--teal);display:flex;align-items:center;justify-content:center;font-size:22px;font-weight:400}
.btn .label{flex:1;background:var(--deep);display:flex;align-items:center;justify-content:center}
.band-sky{top:896px;left:0;width:1200px;height:305px;background:var(--sky)}
.section-title{font-weight:700;color:var(--navy);font-size:38px}
.tile{width:293px;height:252px;color:#fff;padding:38px 40px}
.tile h3{font-weight:400;font-size:22px;line-height:29px;text-transform:uppercase}
.tile p{font-size:13.5px;line-height:20px;margin-top:18px}
.tile a{position:absolute;left:40px;bottom:32px;color:#fff;font-size:13.5px}
.blue{background:var(--card-blue)}.teal{background:var(--card-teal)}.cyan{background:var(--card-cyan)}
.band-mint{top:2476px;left:0;width:1200px;height:351px;background:var(--mint)}
.stat{width:214px;height:214px;text-align:center}
.stat svg{position:absolute;left:0;top:0}
.stat b{position:absolute;left:0;right:0;top:56px;font-weight:900;font-size:45px;color:var(--navy)}
.stat span{position:absolute;left:0;right:0;top:127px;font-size:14px;color:#222;text-transform:uppercase}
.band-navy{top:3380px;left:0;width:1200px;height:663px;background:var(--deep);color:#fff}
.field{border-bottom:1.5px solid #b9c8e6;font-size:12.5px;color:#fff;padding-bottom:20px}
.chat{left:1148px;top:3687px;width:52px;height:52px;background:var(--teal);display:flex;align-items:center;justify-content:center}
.footer{top:4096px;left:0;width:1200px;text-align:center;font-size:13.5px;color:#333}
</style>
</head>
<body>
<header>
  <div class="abs logo">TORVELLA CAPITAL</div>
  <nav class="abs nav">
    <a class="active" href="#">Home</a><a href="#">Expertise</a><a href="#">Story</a><a href="#">Clients</a><a href="#">Approach</a><a href="#">Blog</a><a href="#">Contact</a>
  </nav>
</header>

<div class="abs social" style="top:317px" aria-label="Social link"></div>
<div class="abs social" style="top:359px" aria-label="Social link"></div>
<div class="abs social" style="top:403px" aria-label="Social link"></div>

<div class="abs photo hero" role="img" aria-label="Silhouettes of business people in front of a glowing globe and city skyline"></div>

<section class="abs card" style="left:471px;top:411px;width:533px;height:362px">
  <h2 style="left:43px;top:42px">OUR STORY</h2>
  <div class="line" style="left:43px;top:127px"></div>
  <p style="left:141px;top:118px;width:354px">Torvella Capital is a venture capital studio firm based in Austin TX with a laser focus on raising solid capital for startups and helping businesses jumpstart their revenue. Founded in 2020 by investment expert Marcus Torvell, Torvella Capital combines proven experience in the venture capital field with a data-driven business analysis strategy to secure capital and reinforce revenue streams for startups and established businesses.</p>
</section>
<div class="abs btn" style="left:841px;top:773px;width:163px"><span class="plus">+</span><span class="label">Read More</span></div>

<div class="abs band-sky"></div>
<h2 class="abs section-title" style="left:144px;top:980px">AREA OF EXPERTISE</h2>

<div class="abs tile blue" style="left:144px;top:1075px"><h3>Network<br>Support</h3><p>Help you build your network, introducing you to the right people in the right places.</p><a href="#">+ Learn More</a></div>
<div class="abs tile teal" style="left:453px;top:1075px"><h3>Marketing</h3><p>Consult on marketing process, strategies and implementation across your startup.</p><a href="#">+ Learn More</a></div>
<div class="abs tile cyan" style="left:761px;top:1075px"><h3>Raising<br>Capital</h3><p>Reach out to our extensive connections to raise vital capital for your startup.</p><a href="#">+ Learn More</a></div>
<div class="abs tile cyan" style="left:144px;top:1342px"><h3>Mergers &amp;<br>Acquistions</h3><p>Facilitate a smooth mergers and acquisition process for the expansion of your business.</p><a href="#">+ Learn More</a></div>
<div class="abs tile blue" style="left:453px;top:1342px"><h3>Revenue<br>Acceleration</h3><p>Analyze your revenue streams, providing solutions for kick-starting your revenue.</p><a href="#">+ Learn More</a></div>
<div class="abs tile teal" style="left:761px;top:1342px"><h3>Integration &amp;<br>Incubation</h3><p>Providing training and guidance for startups looking to make their mark on the world.</p><a href="#">+ Learn More</a></div>

<div class="abs photo meeting" role="img" aria-label="Overhead view of business partners shaking hands across a desk with charts and a laptop"></div>

<section class="abs card" style="left:471px;top:1994px;width:533px;height:362px">
  <h2 style="left:43px;top:42px">Blog Posts</h2>
  <div class="line" style="left:43px;top:127px"></div>
  <div class="abs" style="left:141px;top:120px;width:360px;font-size:20px;line-height:26px;color:#111">Totam rem aperiam, eaque ipsa quae ab illo inventore veritatis et</div>
  <div class="abs" style="left:140px;top:186px;font-size:13.5px;color:var(--teal)">February 21,2022</div>
  <p style="left:141px;top:220px;width:354px">Sed ut perspiciatis unde omnis iste natus er voluptatem accusantium doloremque laudantium, totam rem aperiam, eaque ipsa quae ab illo inventore veritatis et quasi architecto beatae vitae dicta sunt explicabo.</p>
</section>
<div class="abs btn" style="left:841px;top:2356px;width:163px"><span class="plus">+</span><span class="label">View More</span></div>

<div class="abs band-mint"></div>
<div class="abs stat" style="left:150px;top:2553px"><svg width="214" height="214"><circle cx="107" cy="107" r="103" fill="none" stroke="var(--rule)" stroke-width="5"/><circle cx="107" cy="107" r="103" fill="none" stroke="var(--navy)" stroke-width="5" stroke-dasharray="130 600" transform="rotate(-180 107 107)"/></svg><b>$40M+</b><span>Money Raised</span></div>
<div class="abs stat" style="left:385px;top:2553px"><svg width="214" height="214"><circle cx="107" cy="107" r="103" fill="none" stroke="var(--rule)" stroke-width="5"/><circle cx="107" cy="107" r="103" fill="none" stroke="var(--teal)" stroke-width="5" stroke-dasharray="95 600" transform="rotate(-135 107 107)"/></svg><b>$125M+</b><span>Attributed Revenue</span></div>
<div class="abs stat" style="left:617px;top:2553px"><svg width="214" height="214"><circle cx="107" cy="107" r="103" fill="none" stroke="var(--rule)" stroke-width="5"/><circle cx="107" cy="107" r="103" fill="none" stroke="var(--navy)" stroke-width="5" stroke-dasharray="230 600" transform="rotate(-230 107 107)"/></svg><b>11</b><span>Company Exits</span></div>
<div class="abs stat" style="left:850px;top:2553px"><svg width="214" height="214"><circle cx="107" cy="107" r="103" fill="none" stroke="var(--rule)" stroke-width="5"/><circle cx="107" cy="107" r="103" fill="none" stroke="var(--teal)" stroke-width="5" stroke-dasharray="75 600" transform="rotate(-125 107 107)"/></svg><b>2</b><span>Awards Won</span></div>

<section class="abs card" style="left:146px;top:2899px;width:908px;height:359px">
  <h2 style="left:69px;top:56px">OUR APPROACH</h2>
  <div class="line" style="left:69px;top:140px"></div>
  <p style="left:169px;top:134px;width:595px">We’ve built our approach to helping your startup thrive based around three key developmental pillars that guarantee results for our partners. First pillar is expertise. We’ve built our firm on a bank of insights, knowledge and proficiencies honed over years of working with the biggest names in venture capitalism – that experience forms the backbone of every project, every pitch and every investment.Second pillar is collaboration. We believe that the best partnerships start with a combined and cooperative approach that benefits all parties every step of the way. We’ll always keep our partners up-to-date with our work using regular touchpoints and reports.</p>
</section>
<div class="abs btn" style="left:891px;top:3258px;width:163px"><span class="plus">+</span><span class="label">Read More</span></div>

<section class="abs band-navy">
  <h2 class="abs" style="left:0;width:1200px;top:95px;text-align:center;font-size:36px;font-weight:700">BUILD WITH US</h2>
  <div class="abs field" style="left:173px;top:219px;width:396px">Enter Name</div>
  <div class="abs field" style="left:629px;top:219px;width:396px">Enter Email</div>
  <div class="abs field" style="left:173px;top:306px;width:852px">Enter Phone</div>
  <div class="abs field" style="left:173px;top:393px;width:852px;padding-bottom:64px">Message</div>
  <div class="abs btn" style="left:517px;top:509px;width:164px"><span class="plus" style="background:var(--cyan)">+</span><span class="label" style="background:var(--teal)">Submit</span></div>
</section>

<div class="abs chat" aria-label="Chat"><svg width="22" height="20" viewBox="0 0 22 20"><path d="M11 1C5.5 1 1 4.6 1 9c0 2.2 1.1 4.2 3 5.6L3 19l4.6-2.5c1.1.3 2.2.5 3.4.5 5.5 0 10-3.6 10-8S16.5 1 11 1z" fill="#fff"/><circle cx="7" cy="9" r="1.3" fill="var(--teal)"/><circle cx="11" cy="9" r="1.3" fill="var(--teal)"/><circle cx="15" cy="9" r="1.3" fill="var(--teal)"/></svg></div>

<footer class="abs footer">Copyright © 2021 Torvellacapital.All Rights Reserved &nbsp;|&nbsp; Privacy Policy &nbsp;|&nbsp; Terms and Use</footer>
<svg class="abs" style="left:1024px;top:4092px" width="32" height="18" viewBox="0 0 32 18" aria-label="Back to top"><path d="M2 16L16 3l14 13" fill="none" stroke="var(--navy)" stroke-width="3"/></svg>
</body>
</html>
```